Exciting brochure for new start up in Australia (corporate mentor program)

We are setting up a program called "The Summit Ladder"
The brochure will have the following sections:
Program Framework:
5 Interactive sessions with well-respected CFO (mentor)
- Driving commercial programmes and overcoming barriers
- Executing group strategy and how you can participate
- Leading a transformation
- What does the CFO define as top talent?
- Exploring the career journey to CFO
The program focuses on discussion and insights into the 4 core areas the CFO must master;
1. Strategy & Commercial
2. Operational
3. Decision Making
4. Leadership
(please draw a venn diagram (circles intersecting) using the making one circle representing each other areas noted above. At the intersection (in the middle, please place the term "CFO Success")
Participants
High calibre participants will be hand selected and assessed before joining the program to ensure a "high performance" culture is developed within the program.
As part of the program, participants will be provided with;
- Breakfast and refreshments at each session
- Opportunity to communicate directly with CFO (mentors) in a confidential environment
- Course material and other relevant reading material
- Access to a closed community for networking with other participants (online/ social)
- Access to QEB's "Keystone Circle" which offers recruitment services at discounted rates
- Invites to other social, educational and networking opportunities
Please see the www.qeb.com.au website for branding and logo to use on this document.
Updates
Hi all,
The project is reasonably urgent and I'm looking to review designs of the brochure as soon as possible. If you have any questions on this, please let me know.
I'm looking forward to receiving something soon.
Thanks
TL
Target Market(s)
professionals
Font styles to use
Other font styles liked:
- modern font.. corporate yet contemporary
Requirements
Must have
- ven diagram, descriptions provided, professional image, aligned to the QEB website
Should not have
- soft colours, missing detail

```html
<!DOCTYPE html>
<html lang="en">
<head>
<meta charset="utf-8">
<title>The Summit Ladder – Brochure Cover</title>
<link href="https://fonts.googleapis.com/css2?family=Questrial&display=swap" rel="stylesheet">
<style>
  :root{
    --backdrop:#a8a8a8;
    --paper:#ffffff;
    --orange:#f39523;
    --ink:#2b2b2b;
    --sky-light:#d9ecf8;
    --sky-mid:#6fb0e6;
    --glass-deep:#123a66;
    --puzzle-pale:#eef4fa;
    --puzzle-blue:#b9d3ea;
    --seam:#d4d4d4;
  }
  *{margin:0;padding:0;box-sizing:border-box}
  html,body{width:1200px;height:900px;overflow:hidden}
  body{background:var(--backdrop);position:relative;font-family:"Questrial",sans-serif}
  .cover-spread{
    position:absolute;left:5px;top:220px;width:1187px;height:420px;
    background:var(--paper);
    box-shadow:0 3px 8px rgba(0,0,0,.25);
  }
  .cover-spread svg{position:absolute;inset:0;width:100%;height:100%}
  .contact-block{
    position:absolute;right:620px;top:376px;
    text-align:right;color:var(--ink);font-style:normal;
    font-size:13.5px;line-height:18px;letter-spacing:.1px;
  }
  .brand{
    position:absolute;left:944px;top:108px;
    display:flex;align-items:center;gap:12px;
  }
  .brand-square{width:14px;height:14px;background:var(--orange)}
  .brand-name{
    font-size:54px;line-height:1;color:var(--ink);
    letter-spacing:3px;
  }
</style>
</head>
<body>
  <section class="cover-spread">
    <svg viewBox="0 0 1187 420" xmlns="http://www.w3.org/2000/svg">
      <defs>
        <linearGradient id="teamGrad" x1="0" y1="0" x2="1" y2="1">
          <stop offset="0" stop-color="#eef4fa"/>
          <stop offset="1" stop-color="#b9d3ea"/>
        </linearGradient>
        <linearGradient id="skyGrad" x1="0" y1="1" x2="1" y2="0">
          <stop offset="0" stop-color="#123a66"/>
          <stop offset=".45" stop-color="#2d6fae"/>
          <stop offset="1" stop-color="#6fb0e6"/>
        </linearGradient>
      </defs>

      <g role="img" aria-label="Photo of business people standing on jigsaw puzzle pieces">
        <polygon points="0,0 295,0 435,110 0,380" fill="url(#teamGrad)"/>
      </g>
      <g role="img" aria-label="Close-up of light blue jigsaw puzzle pieces">
        <polygon points="295,0 593,0 593,5 435,110" fill="var(--sky-light)"/>
      </g>
      <polygon class="accent-triangle" points="435,110 593,5 593,232" fill="var(--orange)"/>

      <polygon class="accent-triangle" points="593,0 865,0 745,110" fill="var(--orange)"/>
      <g role="img" aria-label="Photo looking up at glass office towers against a blue sky with clouds">
        <polygon points="593,0 745,110 1187,420 593,420" fill="url(#skyGrad)"/>
      </g>

      <line class="page-seam" x1="593.5" y1="0" x2="593.5" y2="420" stroke="var(--seam)" stroke-width="1"/>
    </svg>

    <address class="contact-block">
      Level 7, 18 Harbourview Lane, Sydney NSW, Australia 2000<br>
      Phone:+61 2 9000 4417
    </address>

    <div class="brand">
      <span class="brand-square"></span>
      <span class="brand-name">QEB</span>
    </div>
  </section>
</body>
</html>
```